Start-up consultancy in Healthcare Space requiring clean and crisp website design

I am the founder of a start-up consultancy to improve access to medicines and healthcare around the globe. My primary product are consulting services to both the public sector and the private sector to work on: improved healthcare delivery, the right price for medicines and addressing challenges in emerging markets. As the sector is fairly conservative, I need a clean and very professional website as is should signal competence in the sector. Therefore, I like shades of white and green but there should be a link to healthcare. Please see the logo that is featured on my business cards.

Target Market(s)

Ministry of Health, Pharmaceutical companies, Emerging Markets (Latin America, Middle East, Eastern Europe, Asia)

Industry/Entity Type

Healthcare

Coding

Coded - Design and coding required

Number of Pages Required

5+ page

Font styles to use
Serif

Colors

Designer to choose colors to be used in the design.

Requirements
Must have
• About Section
• Services Section
• Blog Section
• The website design should also portray the solution for access to healthcare and highlight my ability to help clients with that.
• The website will be hosted on a CMS and should therefore be easy to adjust. I would prefer wordpress but open to any suggestions as I have my own webspace.
• I quite like these websites:
• https://www.tevluma.com/why-tevluma
• https://home.quillfernwell.com/
Nice to have
• I like to see some creative thinking with the theme of healthcare.
Should not have
• The design should not feature too many hospitals or pills etc. as this is really not my focus.

```html
<!DOCTYPE html>
<html lang="en">
<head>
<meta charset="utf-8">
<title>Veradon Consulting</title>
<link rel="stylesheet" href="https://fonts.googleapis.com/css2?family=Cinzel:wght@400;700&family=Open+Sans:wght@400;600;700&display=swap">
<style>
:root{
  --green:#0d6b3b;
  --green-dark:#0a5a31;
  --ink:#222;
  --body:#666;
  --light:#f3f3f3;
  --white:#fff;
  --rule:#dcdcdc;
}
*{box-sizing:border-box;margin:0;padding:0}
html,body{width:1200px;height:2620px;overflow:hidden;background:var(--white)}
body{position:relative;font-family:"Open Sans",Arial,sans-serif;color:var(--ink)}
.abs{position:absolute}

/* header */
.topline{top:0;left:0;width:1200px;height:4px;background:var(--green)}
.site-header{top:4px;left:0;width:1200px;height:83px;background:var(--white);z-index:3}
.brand-tab{left:82px;top:-52px;width:218px;height:218px;border-radius:50%;background:var(--white);z-index:4;
  display:flex;align-items:flex-end;justify-content:center;padding-bottom:52px}
.brand-name{font-family:"Cinzel",Georgia,serif;font-weight:700;color:var(--green);font-size:25px;line-height:1.05;text-align:center}
.main-nav{top:34px;left:0;width:1200px;font-family:"Cinzel",Georgia,serif;font-size:16px;font-weight:700}
.main-nav a{position:absolute;color:var(--ink);text-decoration:none;white-space:nowrap}
.main-nav a.active{color:var(--green)}
.search-icon{left:932px;top:38px}
.signup{left:990px;top:26px;width:111px;height:40px;border-radius:20px;background:var(--green);color:var(--white);
  font-size:13px;font-weight:700;display:flex;align-items:center;justify-content:center;gap:6px}

/* hero */
.hero{top:87px;left:0;width:1200px;height:483px;
  background:linear-gradient(100deg,#8d8f8f 0%,#b7b9b8 30%,#9fb3a8 55%,#6f9e88 75%,#b6cfc4 100%)}
.hero-title{left:100px;top:230px;font-family:"Cinzel",Georgia,serif;font-weight:700;font-size:44px;color:var(--white)}
.hero-sub{left:100px;top:300px;font-size:22px;line-height:35px;font-weight:600;color:var(--white)}
.btn-outline{border:2px solid var(--white);border-radius:22px;color:var(--white);font-weight:700;font-size:15px;
  display:flex;align-items:center;justify-content:center}
.hero-btn{left:100px;top:393px;width:162px;height:40px}
.dots{left:565px;top:513px;display:flex;gap:6px}
.dots span{width:11px;height:11px;border-radius:50%;border:2px solid var(--white)}
.dots span.on{background:var(--white)}

/* section headings */
.section-title{left:0;width:1200px;text-align:center;font-family:"Cinzel",Georgia,serif;font-weight:700;font-size:28px;color:var(--ink)}
.section-title em{font-style:normal;color:var(--green)}

/* welcome */
.intro{left:220px;width:760px;top:700px;text-align:center;font-size:12.5px;line-height:26px;color:var(--body)}
.feature{width:340px;text-align:center}
.feature-art{width:130px;height:113px;margin:0 auto;border-radius:14px}
.feature h3{margin-top:48px;font-family:"Cinzel",Georgia,serif;font-weight:700;font-size:18px;letter-spacing:.5px}
.feature p{margin-top:20px;font-size:12.5px;line-height:23px;color:var(--body)}
.read-more{display:block;margin-top:16px;font-size:12px;font-weight:700;color:var(--green)}

/* how it works */
.how{top:1198px;left:0;width:1200px;height:793px;background:var(--light)}
.step{width:360px}
.step h4{font-family:"Cinzel",Georgia,serif;font-weight:700;font-size:18px;letter-spacing:.5px}
.step p{margin-top:14px;font-size:12.5px;line-height:26px;color:var(--body)}
.step.left{text-align:right}
.step-art{width:150px;height:150px;border-radius:50%;border:4px solid var(--white);box-shadow:0 0 0 2px #dadada}

/* cta */
.cta-band{top:1991px;left:0;width:1200px;height:297px;background:linear-gradient(90deg,#0f6e3c,#1f7d4c 50%,#0f6e3c)}
.cta-title{top:2050px;left:0;width:1200px;text-align:center;font-family:"Cinzel",Georgia,serif;font-weight:700;font-size:26px;letter-spacing:.5px;color:var(--white)}
.cta-text{top:2102px;left:270px;width:660px;text-align:center;font-size:12.5px;line-height:24px;color:var(--white)}
.cta-btn{top:2177px;left:517px;width:166px;height:43px}

/* footer */
.footer-brand{top:2385px;left:0;width:1200px;text-align:center;font-family:"Cinzel",Georgia,serif;font-weight:700;font-size:34px;color:var(--green)}
.footer-nav{top:2496px;left:0;width:1200px;text-align:center;font-size:15px;color:var(--ink)}
.footer-nav span{margin:0 12px}
.footer-rule{top:2545px;left:97px;width:1005px;height:1px;background:var(--rule)}
.copyright{top:2573px;left:97px;font-size:12px;color:var(--ink)}
.social{top:2563px;left:935px;display:flex;gap:6px}
.social span{width:38px;height:38px;border-radius:50%;border:1px solid #555}
</style>
</head>
<body>

<div class="abs topline"></div>
<header class="abs site-header">
  <nav class="abs main-nav">
    <a class="active" style="left:426px">Home</a>
    <a style="left:508px">About us</a>
    <a style="left:620px">Services</a>
    <a style="left:722px">Blog</a>
    <a style="left:800px">Contact us</a>
  </nav>
  <svg class="abs search-icon" width="16" height="16" viewBox="0 0 16 16" aria-label="Search"><circle cx="6.5" cy="6.5" r="5" fill="none" stroke="#222" stroke-width="2"/><line x1="10" y1="10" x2="15" y2="15" stroke="#222" stroke-width="2.4"/></svg>
  <div class="abs signup">
    <svg width="11" height="13" viewBox="0 0 11 13"><rect x="0" y="5.5" width="11" height="7.5" rx="1" fill="#fff"/><path d="M2.5 5.5V4a3 3 0 0 1 6 0v1.5" fill="none" stroke="#fff" stroke-width="1.6"/></svg>
    SIGN UP
  </div>
</header>
<div class="abs brand-tab"><div class="brand-name">Veradon<br>Consulting</div></div>

<section>
  <div class="abs hero" role="img" aria-label="Gloved hand of a doctor with a stethoscope, overlaid by a world map of connected network points and a compass"></div>
  <h1 class="abs hero-title">Veradon Consulting</h1>
  <p class="abs hero-sub">We are a consultancy to improve access to medicines<br>and healthcare around the globe</p>
  <div class="abs btn-outline hero-btn">GET A QUOTE</div>
  <div class="abs dots"><span class="on"></span><span></span><span></span><span></span></div>
</section>

<section>
  <h2 class="abs section-title" style="top:637px">Welcome to <em>Veradon Consulting</em></h2>
  <p class="abs intro">At vero eos et accusamus et iusto odio dignissimos ducimus qui blanditiis praesentium voluptatum deleniti atque corrupti quos dolores et quas molestias excepturi sint occaecati cupiditate non provident, similique sunt in culpa qui officia deserunt mollitia</p>

  <div class="abs feature" style="left:64px;top:804px">
    <div class="feature-art" role="img" aria-label="Red first aid kit illustration" style="background:#e0504a"></div>
    <h3>Healthcare Delivery</h3>
    <p>Nam libero tempore, cum soluta nobis<br>eligendi optio cumque nihil impedit quo minq<br>uod maxime placeat facere lupt</p>
    <span class="read-more">READ MORE &gt;&gt;</span>
  </div>
  <div class="abs feature" style="left:429px;top:804px">
    <div class="feature-art" role="img" aria-label="Green price tag illustration" style="background:#8aa33a"></div>
    <h3>Right Price for Medicines</h3>
    <p>Nam libero tempore, cum soluta nobis<br>eligendi optio cumque nihil impedit quo minq<br>uod maxime placeat facere lupt</p>
    <span class="read-more">READ MORE &gt;&gt;</span>
  </div>
  <div class="abs feature" style="left:794px;top:804px">
    <div class="feature-art" role="img" aria-label="Handshake illustration" style="background:linear-gradient(90deg,#5bc3d1,#8a8a8a,#ec8a2e)"></div>
    <h3>Addressing Challenges</h3>
    <p>Nam libero tempore, cum soluta nobis<br>eligendi optio cumque nihil impedit quo minq<br>uod maxime placeat facere lupt</p>
    <span class="read-more">READ MORE &gt;&gt;</span>
  </div>
</section>

<section>
  <div class="abs how"></div>
  <h2 class="abs section-title" style="top:1262px">How It <em>Works</em></h2>

  <svg class="abs" style="left:590px;top:1492px" width="20" height="300" viewBox="0 0 20 300">
    <line x1="10" y1="0" x2="10" y2="60" stroke="#bbb" stroke-width="2"/>
    <polyline points="4,20 10,26 16,20" fill="none" stroke="#999" stroke-width="2"/>
    <line x1="10" y1="212" x2="10" y2="268" stroke="#bbb" stroke-width="2"/>
    <polyline points="4,232 10,238 16,232" fill="none" stroke="#999" stroke-width="2"/>
  </svg>

  <div class="abs step-art" role="img" aria-label="Hand holding a phone with healthcare app icons" style="left:524px;top:1343px;background:#7fd0ea"></div>
  <div class="abs step-art" role="img" aria-label="Laptop with doctor video call illustration" style="left:524px;top:1553px;background:#7fcfc6"></div>
  <div class="abs step-art" role="img" aria-label="Prescription clipboard illustration" style="left:524px;top:1761px;background:#8fb3d6"></div>

  <div class="abs step left" style="left:73px;top:1368px">
    <h4>Grab your phone &amp; open the app</h4>
    <p>Nam libero tempore, cum soluta nobis est elendi<br>optio cumque nihil impedit quo minus</p>
  </div>
  <div class="abs step" style="left:767px;top:1600px">
    <h4>Request a call from a doctor</h4>
    <p>Nam libero tempore, cum soluta nobis est elendi<br>optio cumque nihil impedit quo minus</p>
  </div>
  <div class="abs step left" style="left:73px;top:1792px">
    <h4>Pick up prescriptions</h4>
    <p>Nam libero tempore, cum soluta nobis est elendi<br>optio cumque nihil impedit quo minus</p>
  </div>
</section>

<section>
  <div class="abs cta-band" role="img" aria-label="Green tinted photo of hands holding a smartphone"></div>
  <h2 class="abs cta-title">Find the right price for medicines</h2>
  <p class="abs cta-text">Nam libero tempore, cum soluta nobis est eligendi optio cumque nihil impedit quo minus id quod maxime plac eat facere possimus, omnis voluptas assumenda est, omnis dolor repellendus.</p>
  <div class="abs btn-outline cta-btn">GET STARTED</div>
</section>

<footer>
  <div class="abs footer-brand">Veradon Consulting</div>
  <div class="abs footer-nav">HOME<span>|</span>ABOUT US<span>|</span>SERVICES<span>|</span>BLOG<span>|</span>CONTACT US</div>
  <div class="abs footer-rule"></div>
  <p class="abs copyright">© 2017, Veradon Consulting. Privacy Policy | Terms of Use</p>
  <div class="abs social" aria-label="Social links"><span></span><span></span><span></span><span></span></div>
</footer>

</body>
</html>
```